Washing Up Liquid Label

We are looking for 2 labels to be designed to be part of a range of products.

The brand is Marlow Brite and we are looking for a label design to you on washing up liquid bottle similar to the ones in the file attached.

One label it be original and the liquid will be green so the label colour needs to be green or work with the green. The other label is lemon and is yellow.

Please see attached the Marlow Brite logo and also a couple of the other designs in the range.

```html
<!DOCTYPE html>
<html lang="en">
<head>
<meta charset="utf-8">
<title>Marlow Brite Dishwashing Liquid Labels</title>
<link rel="stylesheet" href="https://fonts.googleapis.com/css2?family=Kaushan+Script&display=swap">
<style>
  :root {
    --bg: #e4e4e4;
    --green-deep: #5f9128;
    --green-mid: #79ab3c;
    --green-light: #a3c966;
    --ring-yellow: #d9d868;
    --ring-gold: #e8c93a;
    --brand-blue: #1f4fa6;
    --brand-light: #ffffff;
    --new-red: #b3121c;
    --script-yellow: #f0d85a;
    --script-green: #3f8a22;
    --splash-dark: #0d2a6e;
    --splash-mid: #2f7fd0;
    --splash-light: #e6f4ff;
  }
  html, body {
    margin: 0;
    width: 1200px;
    height: 904px;
    overflow: hidden;
    background: var(--bg);
  }
  .label-sheet { display: block; width: 1200px; height: 904px; }
  .script { font-family: "Kaushan Script", cursive; }
  .brand-name { fill: var(--brand-blue); font-size: 25px; }
  .brand-name-light { fill: var(--brand-light); }
  .flag-new { fill: var(--new-red); font-size: 26px; }
  .product-original { fill: var(--script-yellow); font-size: 28px; }
  .product-lemon { fill: var(--script-green); font-size: 28px; }
</style>
</head>
<body>
<svg class="label-sheet" viewBox="0 0 1200 904" xmlns="http://www.w3.org/2000/svg">
  <defs>
    <radialGradient id="original-face" cx="0.45" cy="0.4" r="0.65">
      <stop offset="0" stop-color="var(--green-light)"/>
      <stop offset="1" stop-color="var(--green-mid)"/>
    </radialGradient>
    <linearGradient id="lemon-splash" x1="0" y1="0" x2="1" y2="1">
      <stop offset="0" stop-color="var(--splash-dark)"/>
      <stop offset="0.45" stop-color="var(--splash-mid)"/>
      <stop offset="0.75" stop-color="var(--splash-light)"/>
      <stop offset="1" stop-color="var(--splash-mid)"/>
    </linearGradient>
  </defs>

  <g class="label label-original">
    <circle cx="458" cy="567" r="122" fill="var(--ring-yellow)"/>
    <circle cx="458" cy="567" r="116" fill="var(--green-deep)"/>
    <circle cx="458" cy="567" r="108" fill="none" stroke="var(--ring-yellow)" stroke-width="3"/>
    <circle cx="458" cy="567" r="100" fill="url(#original-face)"/>
    <text class="script brand-name" x="458" y="532" text-anchor="middle">Marlow Brite</text>
    <text class="script flag-new" x="405" y="577" text-anchor="middle">New!</text>
    <text class="script product-original" x="458" y="613" text-anchor="middle">Dishwashing</text>
    <text class="script product-original" x="470" y="647" text-anchor="middle">Liquid</text>
  </g>

  <g class="label label-lemon">
    <circle cx="803" cy="592" r="118" fill="var(--green-mid)"/>
    <circle cx="803" cy="592" r="110" fill="var(--ring-gold)"/>
    <circle cx="803" cy="592" r="104" fill="url(#lemon-splash)" role="img" aria-label="Photo of sparkling clean glassware in a blue water splash"/>
    <text class="script brand-name brand-name-light" x="803" y="557" text-anchor="middle">Marlow Brite</text>
    <text class="script flag-new" x="750" y="602" text-anchor="middle">New!</text>
    <text class="script product-lemon" x="803" y="638" text-anchor="middle">Dishwashing</text>
    <text class="script product-lemon" x="815" y="672" text-anchor="middle">Liquid</text>
  </g>
</svg>
</body>
</html>
```